Advertisement Design Project

Attached is the information I need in a big color ad

10X11 that will go in a weekly local paper.
I am open to color and graphics-no pictures of people please.

My logo is also attached, which I would like in the ad.

Sorry for the short notice-I just got a deal on the space and it is due Friday.

```html
<!DOCTYPE html>
<html lang="en">
<head>
<meta charset="utf-8">
<title>Trusts, New Tax Laws – Workshop Ad</title>
<link href="https://fonts.googleapis.com/css2?family=Oswald:wght@700&family=Roboto+Condensed:ital,wght@0,400;0,700;1,700&display=swap" rel="stylesheet">
<style>
  :root {
    --gold: #fbb829;
    --gold-soft: #fde2a5;
    --charcoal: #464646;
    --ink: #2b2b2b;
    --paper: #ffffff;
    --backdrop: #d9d9d9;
  }
  * { box-sizing: border-box; margin: 0; padding: 0; }
  html, body { width: 1200px; height: 1000px; overflow: hidden; background: var(--backdrop); }
  .ad {
    position: absolute; left: 170px; top: 28px; width: 832px; height: 944px;
    background: var(--paper); overflow: hidden;
    font-family: "Roboto Condensed", "Arial Narrow", sans-serif; color: var(--ink);
  }
  .headline {
    position: absolute; left: 0; width: 100%; top: 18px; text-align: center;
    font-family: "Oswald", "Arial Narrow", sans-serif; font-weight: 700;
    font-size: 84px; line-height: 96px; color: var(--gold); letter-spacing: -1px;
  }
  .subhead {
    position: absolute; left: 0; width: 100%; top: 106px; text-align: center;
    font-family: "Oswald", "Arial Narrow", sans-serif; font-weight: 700;
    font-size: 52px; line-height: 64px; color: var(--charcoal);
  }
  .hero-photo {
    position: absolute; left: 120px; top: 170px; width: 615px; height: 272px;
    background: radial-gradient(ellipse at 45% 55%, #c79a5a 0%, #a4b79a 35%, #eef0ea 70%, #ffffff 100%);
  }
  .intro {
    position: absolute; left: 48px; top: 456px;
    font-weight: 700; font-style: italic; font-size: 31px; color: var(--charcoal);
  }
  .questions { position: absolute; left: 48px; top: 503px; list-style: none; }
  .questions li {
    position: relative; padding-left: 28px; height: 27.3px; line-height: 27.3px;
    font-weight: 700; font-style: italic; font-size: 16px; color: var(--ink);
  }
  .questions li::before {
    content: ""; position: absolute; left: 0; top: 7px; width: 14px; height: 14px;
    border-radius: 50%; background: var(--gold);
  }
  .details { position: absolute; left: 482px; top: 500px; width: 340px; }
  .label { font-weight: 700; font-style: italic; font-size: 19px; color: var(--gold); line-height: 28px; }
  .presenter { font-weight: 700; font-style: italic; font-size: 18px; line-height: 28px; color: var(--ink); }
  .info { font-size: 16px; line-height: 29px; color: var(--ink); }
  .workshop { margin-top: 10px; }
  .values {
    position: absolute; left: 480px; top: 815px; width: 328px; height: 26px;
    background: var(--gold-soft); border-radius: 13px;
    display: flex; align-items: center; justify-content: center; gap: 10px;
    font-weight: 700; font-style: italic; font-size: 19px; color: var(--ink);
  }
  .values .dot { width: 11px; height: 11px; border-radius: 50%; background: var(--gold); }
  .footer-band {
    position: absolute; left: 0; bottom: 0; width: 100%; height: 74px; background: var(--gold);
  }
  .motto {
    position: absolute; left: 48px; top: 878px;
    font-weight: 700; font-style: italic; font-size: 15px; line-height: 23px; color: var(--ink);
  }
  .reservation {
    position: absolute; left: 578px; top: 880px; font-size: 16px; line-height: 22px; color: var(--ink);
  }
  .reservation .phone { font-weight: 700; font-style: italic; font-size: 20px; }
  .brand-mark {
    position: absolute; left: 402px; top: 812px; width: 80px; height: 80px; border-radius: 50%;
    background: var(--paper); display: flex; align-items: center; justify-content: center;
    text-align: center; font-weight: 700; font-size: 13px; line-height: 15px; color: var(--charcoal);
  }
</style>
</head>
<body>
  <main class="ad">
    <h1 class="headline">Trusts, New Tax Laws</h1>
    <h2 class="subhead">Annuities and Long Term Care</h2>
    <div class="hero-photo" role="img" aria-label="Glass jar full of coins resting on banknotes with a small model house behind it"></div>

    <p class="intro">Come learn what you need to know</p>
    <ul class="questions">
      <li>Is a living trust right for me?</li>
      <li>Does my existing Trust need to be changed?</li>
      <li>Why does Joint Tenancy create tax problems?</li>
      <li>I have a will, isn’t that enough?</li>
      <li>Why do I need powers of attorney?</li>
      <li>How much are inheritance taxes?</li>
      <li>What are the new Affordable Care Act taxes?</li>
      <li>How does Long Term Care insurance work?</li>
      <li>How does Long Term Care insurance work?</li>
      <li>how do I plan for those costs?</li>
      <li>The truth about annuites-</li>
      <li>What are the biggest mistakes in estate planning?</li>
    </ul>

    <section class="details">
      <p class="label">Presented by:</p>
      <p class="presenter">marla jean whitford</p>
      <p class="presenter">Attorney at Law</p>
      <p class="info">2140 Harbor Lane, Brookvale.</p>
      <p class="info">Helping&nbsp; Families plan their estates for over 20 years.</p>
      <p class="label workshop">Workshop</p>
      <p class="info">on September 19, 2013</p>
      <p class="info">at 1-2:30pm &amp;&nbsp; 6-7:30pm</p>
      <p class="info">Venue : Harborview Inn Brookvale</p>
      <p class="info">4200 Cedar Ridge Court, Brookvale, California 95000</p>
    </section>

    <div class="values">
      <span>Trust</span><span class="dot"></span><span>Relationship</span><span class="dot"></span><span>Integrity</span>
    </div>

    <div class="footer-band"></div>
    <p class="motto">Security =Good information+Good Planning<br>Be Smart. Plan Ahead.</p>
    <div class="brand-mark">Whitford<br>Law</div>
    <p class="reservation">Seating is limited for a Reservation,<br>Please call: <span class="phone">(555) 014 - 2700</span></p>
  </main>
</body>
</html>
```